In need of a production and engineering website design

In need of a website design for my Rap/Hip-Hop Production & Engineering Business. Name can be changed, to fit the idea of the best design but must closely resemble the idea of the first name (ex. Loops by Tavel, Prod. By Tavel, etc.).

The text and design will be in any format but must be eye catching and appeal to a young audience (i.e. attractive design), to include functions preview beats player, clickable catalog for purchasing (using Cashlyn) and a "request for booking" tab for artists, to be used in email format as supposed to a contact me form. Please use generalization tabs such as "Catalog" instead of "buy" or "sell" as these terms do not fit the business model. You may also use "Purchase Beats" instead of Catalog; whatever fits your design will work.

Social Media Links (Chirpex, ViewReel, Pagemoot, AudioDrift, Quorvo+, Flickpost, Careerly (professional resource), etc.) and FAQ page as supposed to a who am I page (bio);

Note: FAQ Page wont be necessary needed for the design portion but would be nice to let the designer know my intentions.

Please use the supplied logo and/or images for your project.

The final design should communicate production/engineer knowledge and potential for music industry growth. (the logo will communicate the same)

Project Deadline Extended Reason: To Provide more time to the competition; To Provide stock pictures and logo designs to make competition more challenging. Added Sunday, June 26, 2016

This site has not been finished by the current designer. He has lacked the necessary communication, implementation of above directives and has neglected to professionally develop and finish the site. Though he has been hired to code the site. His negligence reflects great discredit upon his work and will receive a bad review with this site as reference. He may try to fix his reviews or change his name...either way, I will be there to reference this site as his handiwork. Thanks guy but you did not finish coding the site...which means your dedication to code and development has not finished and I will be looking to recoup the one-on-one if you decide to keep avoiding to finish the previously mentioned and direct messaged objectives which took a whole team to decide on. Thanks.

Target Market(s)

A&R Management Firms (Music), Musicians, Music Artists, Business Entrepreneurs, Etc.

Industry/Entity Type

Music Download

Number of Pages Required

5+ page

Requirements
Must have
• Preview, Select, and Pay options (beats catalog), Bio, Mix/Mastering Services, Contact, Live Talvo Chat, Social Media Networking, FAQ / TOS, the option to code all the work (will add the additional fee to the winning artist), the ability to exchange user's email in return for a free HQ lease of their choice every month starting the 30th day of each month as long as they maintain their subscription status.
Nice to have
• General Merchandise page and a user / admin login and register system buttons and a dedicated blog page (if hired to code, this will be a requirement).
• Those will receive a review if designed: Cell Phone condensed version (w/ buttons to lease and buy on the left side of each song within the playlist)
Should not have
• Copyrighted material, anything not of this generation but must have a keen resemblance of the 2000's to 2010's hip hop trap or rap community.

```html
<!DOCTYPE html>
<html lang="en">
<head>
<meta charset="utf-8">
<title>Loops by Tavel — Beats Catalog</title>
<link href="https://fonts.googleapis.com/css2?family=Raleway:wght@500;700;800&family=Open+Sans:wght@400;600;700&display=swap" rel="stylesheet">
<style>
:root{
  --red:#e2353f;
  --ink:#2d2d2d;
  --muted:#8a8a8a;
  --page:#ececec;
  --line:#d2d2d2;
  --btn-gray:#5f5f5f;
  --player:#c9c9c9;
  --free:#e06a72;
  --lease:#62a12a;
  --premium:#66a7bd;
  --full:#c89c43;
  --footer:#1b1b1d;
  --green:#4c9a2a;
  --star:#e3b21d;
}
*{box-sizing:border-box;margin:0;padding:0}
html,body{width:1200px;height:2980px;overflow:hidden}
body{position:relative;background:var(--page);font-family:"Open Sans",Arial,sans-serif;color:var(--ink)}
.abs{position:absolute}
.topline{top:0;left:0;width:1200px;height:4px;background:var(--red)}
.site-header{top:4px;left:0;width:1200px;height:88px;background:#f4f4f4}
.brand{left:98px;top:30px;font-family:"Raleway",sans-serif;font-weight:800;font-size:24px;letter-spacing:.5px;color:#2a2a2a}
.socials{left:566px;top:14px;display:flex;gap:6px}
.socials span{width:30px;height:30px;border-radius:50%;display:block}
.callus{left:848px;top:20px;font-size:14px;font-weight:600;color:#444;display:flex;align-items:center;gap:6px}
.callus b{color:var(--red);font-size:19px;font-weight:700;margin-left:6px}
.nav{right:96px;top:62px;display:flex;gap:24px;font-family:"Raleway",sans-serif;font-weight:700;font-size:13px;color:#2a2a2a}
.nav .on{color:var(--red)}
.hero{top:92px;left:0;width:1200px;height:330px;background:linear-gradient(100deg,#1a1030 0%,#3a2a66 28%,#5c3d8f 50%,#6a2a6a 70%,#b02a52 85%,#2a1a40 100%)}
.hero-title{top:82px;left:0;width:1200px;text-align:center;font-family:"Raleway",sans-serif;font-weight:800;font-size:86px;letter-spacing:4px;color:rgba(255,255,255,.82)}
.hero-sub{top:178px;left:0;width:1200px;text-align:center;font-weight:700;font-size:21px;color:#fff}
.dots{top:288px;left:532px;display:flex;gap:4px}
.dots span{width:32px;height:4px;background:rgba(255,255,255,.55)}
.dots span:first-child{background:var(--red)}
.section-title{top:474px;left:98px;font-family:"Raleway",sans-serif;font-weight:700;font-size:17px}
.add-cart{top:474px;right:98px;font-family:"Raleway",sans-serif;font-weight:700;font-size:13px;color:var(--green)}
.track{left:98px;width:1004px;height:300px;border-bottom:1px solid var(--line)}
.cover{left:0;top:0;width:322px;height:254px}
.info{left:354px;top:0;width:650px}
.track-title{font-family:"Raleway",sans-serif;font-weight:700;font-size:19px;color:#222}
.meta{margin-top:12px;font-size:13px;color:var(--muted);display:flex;gap:10px}
.meta i{font-style:normal;color:#bbb}
.player{margin-top:22px;height:82px;background:var(--player);position:relative}
.player .prog{position:absolute;left:16px;top:16px;width:618px;height:8px;background:#a9a9a9}
.player .prog::before{content:"";position:absolute;left:0;top:0;width:200px;height:8px;background:#555}
.player .ctrl{position:absolute;left:16px;top:40px;display:flex;align-items:center;gap:10px;font-size:11px;color:#555}
.player .vol{width:70px;height:5px;background:#999;position:relative}
.player .vol::before{content:"";position:absolute;left:0;top:0;width:60px;height:5px;background:var(--green)}
.player .end{position:absolute;right:16px;top:40px;font-size:11px;color:#555}
.links{margin-top:14px;display:flex;justify-content:space-between;font-size:11px;color:#444}
.rating span{color:var(--star);letter-spacing:1px;margin-right:8px}
.actions{margin-top:24px;display:flex;align-items:center}
.btn{display:inline-block;height:44px;line-height:44px;width:176px;text-align:center;font-family:"Raleway",sans-serif;font-weight:700;font-size:14px;color:#fff;letter-spacing:.5px}
.btn.gray{background:var(--btn-gray)}
.btn.red{background:var(--red);margin-left:4px}
.shares{margin-left:auto;display:flex;gap:6px;font-size:10px}
.shares span{border:1px solid #bbb;padding:2px 5px;background:#f7f7f7;color:#345}
.shares b{border:1px solid #bbb;padding:2px 5px;background:#fff;font-weight:600;margin-left:-6px;color:#444}
.view-more{top:2108px;left:98px;font-family:"Raleway",sans-serif;font-weight:700;font-size:14px;color:var(--red)}
.pricing{top:2160px;left:0;width:1200px;height:520px;background:#dedede}
.plan{top:82px;width:236px;height:368px;background:#f4f4f4;border:1px solid #d6d6d6;text-align:center}
.plan-head{height:42px;line-height:42px;font-family:"Raleway",sans-serif;font-weight:700;font-size:19px;color:#fff}
.plan-price{height:58px;line-height:58px;background:#e3e3e3;font-weight:700;font-size:28px;color:#2a2a2a}
.plan-price sup{font-size:14px}
.plan-rows{padding:14px 16px 0}
.plan-rows p{font-size:12px;color:#555;height:40px;line-height:40px;border-bottom:1px solid var(--line)}
.plan-rows p b{color:#333}
.plan-free p{border:none;height:34px;line-height:34px;font-weight:700;font-size:13px;color:#333}
.plan-btn{position:absolute;left:58px;bottom:26px;width:118px;height:38px;line-height:38px;color:#fff;font-family:"Raleway",sans-serif;font-weight:700;font-size:13px;border-radius:3px}
.footer{top:2680px;left:0;width:1200px;height:300px;background:var(--footer);color:#cfcfcf}
.f-brand{left:98px;top:110px;font-family:"Raleway",sans-serif;font-weight:800;font-size:34px;color:#e9e9e9}
.f-col h4{font-family:"Raleway",sans-serif;font-weight:700;font-size:16px;color:#fff;margin-bottom:14px}
.f-col li{list-style:none;font-size:12px;line-height:16px;color:#cfcfcf}
.f-col p{font-size:12px;line-height:18px}
.email{margin-top:16px;width:256px;height:32px;background:#eaeaea;color:#999;font-size:12px;padding:8px 10px}
.sub-btn{margin-top:14px;display:inline-block;background:var(--red);color:#fff;font-size:11px;padding:8px 10px;font-weight:600}
.contact-row{display:flex;gap:14px;font-size:12px;margin-bottom:18px;line-height:18px}
.copy{left:98px;top:268px;font-size:11px;color:#aaa}
.talvo{left:930px;top:256px;width:176px;height:30px;background:#2e8ad0;border-radius:3px;color:#fff;font-size:11px;display:flex;align-items:center;padding-left:8px;gap:8px}
.talvo i{width:20px;height:20px;border-radius:50%;background:#fff;display:block}
.dim{top:0;left:0;width:1200px;height:2980px;background:rgba(0,0,0,.14)}
.modal{left:584px;top:502px;width:430px;height:298px;background:#fff;padding:30px 40px}
.modal h3{font-family:"Raleway",sans-serif;font-weight:700;font-size:23px;color:#222}
.opt{margin-top:22px;display:flex;align-items:center;gap:12px;font-size:13px;color:#444}
.radio{width:16px;height:16px;border-radius:50%;border:2px solid #888}
.radio.on{border:none;background:var(--red)}
.promo{margin-top:16px;display:flex;align-items:center;font-size:12px;color:#555}
.promo span{width:146px}
.promo div{width:220px;height:36px;background:#e3e3e3}
.modal-actions{margin-top:22px;display:flex;gap:16px}
.modal-actions span{width:134px;height:40px;line-height:40px;text-align:center;color:#fff;font-family:"Raleway",sans-serif;font-weight:700;font-size:14px}
.close{left:992px;top:480px;width:44px;height:44px;border-radius:50%;background:#fff;border:3px solid #ddd;text-align:center;line-height:38px;font-weight:700;font-size:20px;color:#333}
</style>
</head>
<body>
<div class="abs topline"></div>
<header class="abs site-header">
  <div class="abs brand">LOOPS BY TAVEL</div>
</header>
<div class="abs socials">
  <span style="background:#3b5ea0" role="img" aria-label="Pagemoot"></span>
  <span style="background:#39a6e0" role="img" aria-label="Chirpex"></span>
  <span style="background:#d3232b" role="img" aria-label="ViewReel"></span>
  <span style="background:#dd4b39" role="img" aria-label="Quorvo+"></span>
  <span style="background:#c42a46" role="img" aria-label="Careerly"></span>
  <span style="background:#f26c1d" role="img" aria-label="AudioDrift"></span>
  <span style="background:#d7c524" role="img" aria-label="Flickpost"></span>
</div>
<div class="abs callus">
  <svg width="16" height="16" viewBox="0 0 24 24"><path d="M6 2l4 4-2 3c1 3 4 6 7 7l3-2 4 4-3 4C10 22 2 14 2 5z" fill="#444"/></svg>
  CALL US ON : <b>1 555 010 0101</b>
</div>
<nav class="abs nav">
  <span>HOME</span><span class="on">BEATS CATALOG</span><span>MIX/MASTERING SERVICES</span><span>MUSIC MERCH</span><span>CONTACT</span>
  <svg width="14" height="14" viewBox="0 0 24 24"><circle cx="10" cy="10" r="7" stroke="#222" stroke-width="3" fill="none"/><path d="M15 15l7 7" stroke="#222" stroke-width="3"/></svg>
</nav>

<section class="abs hero" role="img" aria-label="Banner photo of a producer working a mixing desk under purple and pink studio lights">
  <h1 class="abs hero-title">BEATS CATALOG</h1>
  <p class="abs hero-sub">We are into Rap/Hip-Hop Production &amp; Engineering Business</p>
  <div class="abs dots"><span></span><span></span><span></span><span></span></div>
</section>

<h2 class="abs section-title">BEATS CATALOG</h2>
<div class="abs add-cart">ADD TO CART</div>

<article class="abs track" style="top:546px">
  <div class="abs cover" role="img" aria-label="Photo of a DJ in a cap at turntables" style="background:linear-gradient(160deg,#8fa2a8,#3b4a52 60%,#1c2226)"></div>
  <div class="abs info">
    <h3 class="track-title">At vero eos et accusamus et iusto odio dignissimos</h3>
    <div class="meta"><span>♪ Beats / Instrumentals</span><i>|</i><span>East Coast</span><i>|</i><span>♥ Hip Hop</span><i>|</i><span>Old School</span><i>|</i><span>No Comments</span></div>
    <div class="player"><div class="prog"></div><div class="ctrl">▶ <span>00:00</span> ◀ <span class="vol"></span></div><div class="end">00:00</div></div>
    <div class="links"><span>License-prices &nbsp;|&nbsp; Terms &nbsp;|&nbsp; Contact &nbsp;|&nbsp; Alternative player</span><span class="rating"><span>★★★★★</span>( Rating: 5.0/5 )</span></div>
    <div class="actions"><span class="btn gray">LEASE / CASHLYN</span><span class="btn red">SELECT OPTIONS</span>
      <div class="shares"><span>Pagemoot</span><b>200</b><span>Chirpex</span><b>200</b><span>Quorvo+</span><b>200</b></div></div>
  </div>
</article>

<article class="abs track" style="top:858px">
  <div class="abs cover" role="img" aria-label="Photo of a female DJ with headphones in blue and pink light" style="background:linear-gradient(160deg,#2a2a7a,#7a2a8a 55%,#1a1040)"></div>
  <div class="abs info">
    <h3 class="track-title">At vero eos et accusamus et iusto odio dignissimos</h3>
    <div class="meta"><span>♪ Beats / Instrumentals</span><i>|</i><span>East Coast</span><i>|</i><span>♥ Hip Hop</span><i>|</i><span>Old School</span><i>|</i><span>No Comments</span></div>
    <div class="player"><div class="prog"></div><div class="ctrl">▶ <span>00:00</span> ◀ <span class="vol"></span></div><div class="end">00:00</div></div>
    <div class="links"><span>License-prices &nbsp;|&nbsp; Terms &nbsp;|&nbsp; Contact &nbsp;|&nbsp; Alternative player</span><span class="rating"><span>★★★★★</span>( Rating: 5.0/5 )</span></div>
    <div class="actions"><span class="btn gray">LEASE / CASHLYN</span><span class="btn red">SELECT OPTIONS</span>
      <div class="shares"><span>Pagemoot</span><b>200</b><span>Chirpex</span><b>200</b><span>Quorvo+</span><b>200</b></div></div>
  </div>
</article>

<article class="abs track" style="top:1172px">
  <div class="abs cover" role="img" aria-label="Photo of an engineer at a lit mixing console in a dark studio" style="background:linear-gradient(160deg,#1a2a5a,#2a4a9a 50%,#0c1230)"></div>
  <div class="abs info">
    <h3 class="track-title">At vero eos et accusamus et iusto odio dignissimos</h3>
    <div class="meta"><span>♪ Beats / Instrumentals</span><i>|</i><span>East Coast</span><i>|</i><span>♥ Hip Hop</span><i>|</i><span>Old School</span><i>|</i><span>No Comments</span></div>
    <div class="player"><div class="prog"></div><div class="ctrl">▶ <span>00:00</span> ◀ <span class="vol"></span></div><div class="end">00:00</div></div>
    <div class="links"><span>License-prices &nbsp;|&nbsp; Terms &nbsp;|&nbsp; Contact &nbsp;|&nbsp; Alternative player</span><span class="rating"><span>★★★★★</span>( Rating: 5.0/5 )</span></div>
    <div class="actions"><span class="btn gray">LEASE / CASHLYN</span><span class="btn red">SELECT OPTIONS</span>
      <div class="shares"><span>Pagemoot</span><b>200</b><span>Chirpex</span><b>200</b><span>Quorvo+</span><b>200</b></div></div>
  </div>
</article>

<article class="abs track" style="top:1482px">
  <div class="abs cover" role="img" aria-label="Photo of a DJ with headphones under green and orange lights" style="background:linear-gradient(160deg,#b8422a,#4a6a3a 50%,#1a2a22)"></div>
  <div class="abs info">
    <h3 class="track-title">At vero eos et accusamus et iusto odio dignissimos</h3>
    <div class="meta"><span>♪ Beats / Instrumentals</span><i>|</i><span>East Coast</span><i>|</i><span>♥ Hip Hop</span><i>|</i><span>Old School</span><i>|</i><span>No Comments</span></div>
    <div class="player"><div class="prog"></div><div class="ctrl">▶ <span>00:00</span> ◀ <span class="vol"></span></div><div class="end">00:00</div></div>
    <div class="links"><span>License-prices &nbsp;|&nbsp; Terms &nbsp;|&nbsp; Contact &nbsp;|&nbsp; Alternative player</span><span class="rating"><span>★★★★★</span>( Rating: 5.0/5 )</span></div>
    <div class="actions"><span class="btn gray">LEASE / CASHLYN</span><span class="btn red">SELECT OPTIONS</span>
      <div class="shares"><span>Pagemoot</span><b>200</b><span>Chirpex</span><b>200</b><span>Quorvo+</span><b>200</b></div></div>
  </div>
</article>

<article class="abs track" style="top:1792px">
  <div class="abs cover" role="img" aria-label="Photo of a DJ in glasses at decks with blue and violet light" style="background:linear-gradient(160deg,#4a4aa8,#6a3a9a 50%,#1a1a4a)"></div>
  <div class="abs info">
    <h3 class="track-title">At vero eos et accusamus et iusto odio dignissimos</h3>
    <div class="meta"><span>♪ Beats / Instrumentals</span><i>|</i><span>East Coast</span><i>|</i><span>♥ Hip Hop</span><i>|</i><span>Old School</span><i>|</i><span>No Comments</span></div>
    <div class="player"><div class="prog"></div><div class="ctrl">▶ <span>00:00</span> ◀ <span class="vol"></span></div><div class="end">00:00</div></div>
    <div class="links"><span>License-prices &nbsp;|&nbsp; Terms &nbsp;|&nbsp; Contact &nbsp;|&nbsp; Alternative player</span><span class="rating"><span>★★★★★</span>( Rating: 5.0/5 )</span></div>
    <div class="actions"><span class="btn gray">LEASE / CASHLYN</span><span class="btn red">SELECT OPTIONS</span>
      <div class="shares"><span>Pagemoot</span><b>200</b><span>Chirpex</span><b>200</b><span>Quorvo+</span><b>200</b></div></div>
  </div>
</article>

<div class="abs view-more">VIEW MORE &gt;&gt;</div>

<section class="abs pricing">
  <div class="abs plan plan-free" style="left:100px">
    <div class="plan-head" style="background:var(--free)">FREE</div>
    <div class="plan-price">$0</div>
    <div class="plan-rows" style="padding-top:26px"><p>No Units</p><p>listen and no profits</p><p>gained from it.</p></div>
    <span class="plan-btn" style="background:var(--free)">DOWNLOAD</span>
  </div>
  <div class="abs plan" style="left:356px">
    <div class="plan-head" style="background:var(--lease)">LEASE</div>
    <div class="plan-price">$29<sup>99</sup>- $44<sup>90</sup></div>
    <div class="plan-rows"><p><b>1 Profitable</b> Project</p><p>3000 units</p><p><b>Only non-</b>Profitable</p><p>Mechanical License Agreement</p></div>
    <span class="plan-btn" style="background:var(--lease)">SUBSCRIBE</span>
  </div>
  <div class="abs plan" style="left:612px">
    <div class="plan-head" style="background:var(--premium)">PREMIUM LEASE</div>
    <div class="plan-price">$29<sup>99</sup>- $44<sup>90</sup></div>
    <div class="plan-rows"><p><b>1 Profitable</b> Project</p><p>10000 units</p><p><b>Limited-</b>Profitable</p><p>Mechanical License Agreement</p></div>
    <span class="plan-btn" style="background:var(--premium)">SUBSCRIBE</span>
  </div>
  <div class="abs plan" style="left:868px">
    <div class="plan-head" style="background:var(--full)">FULL RIGHTS</div>
    <div class="plan-price">$29<sup>99</sup>- $44<sup>90</sup></div>
    <div class="plan-rows"><p><b>1 Profitable</b> Project</p><p><b>Unlimited units</b> units</p><p><b>100%</b> -Profitable</p><p>Mechanical License Agreement</p></div>
    <span class="plan-btn" style="background:var(--full)">SUBSCRIBE</span>
  </div>
</section>

<footer class="abs footer">
  <div class="abs f-brand">LOOPS BY TAVEL</div>
  <div class="abs f-col" style="left:440px;top:36px">
    <h4>Information</h4>
    <ul><li>Home</li><li>Beats Catalog</li><li>Mix/Mastering Services</li><li>Music Merch</li><li>Blog</li><li>Videos</li><li>Contact</li><li>View Cart</li></ul>
  </div>
  <div class="abs f-col" style="left:638px;top:36px;width:270px">
    <h4>Newsletter Subscription</h4>
    <p>Register your Email Address to Receive a Free Lease! Terms Apply</p>
    <div class="email">Email Address</div>
    <span class="sub-btn">SUBSCRIBE</span>
  </div>
  <div class="abs f-col" style="left:944px;top:36px;width:200px">
    <h4>Contact Us</h4>
    <div class="contact-row"><svg width="12" height="16" viewBox="0 0 12 16"><path d="M6 0a6 6 0 016 6c0 4-6 10-6 10S0 10 0 6a6 6 0 016-6z" fill="#ddd"/><circle cx="6" cy="6" r="2" fill="#1b1b1d"/></svg><span>14 Harbor Lane<br>Millbrook, PA 17090</span></div>
    <div class="contact-row"><svg width="14" height="14" viewBox="0 0 24 24"><path d="M6 2l4 4-2 3c1 3 4 6 7 7l3-2 4 4-3 4C10 22 2 14 2 5z" fill="#ddd"/></svg><span>1 555 010 0101</span></div>
    <div class="contact-row"><svg width="14" height="12" viewBox="0 0 14 12"><rect width="14" height="12" fill="#ddd"/><path d="M0 0l7 6 7-6" stroke="#1b1b1d" fill="none"/></svg><span style="text-decoration:underline">hello@loopsbytavel.com</span></div>
  </div>
  <div class="abs copy">© 2016, Loops by Tavel. All rights reserved.</div>
  <div class="abs talvo"><i></i>Chat with us on Talvo</div>
</footer>

<div class="abs dim"></div>

<div class="abs modal">
  <h3>MAKE YOUR SELECTION</h3>
  <div class="opt"><span class="radio on"></span>Premium Lease</div>
  <div class="opt"><span class="radio"></span>Full Rights</div>
  <div class="promo"><span>Enter Promotion Code</span><div></div></div>
  <div class="modal-actions"><span style="background:var(--red)">CONTINUE</span><span style="background:var(--btn-gray)">CHECKOUT</span></div>
</div>
<div class="abs close">X</div>
</body>
</html>
```